After a very formal and professional busuness card, After high qaulity for high end customers

Larkmere Bathrooms
0487265920
Lic # 582143K
Renovation specialists
Tobin@larkmerebathrooms.com.au

```html
<!DOCTYPE html>
<html lang="en">
<head>
<meta charset="utf-8">
<title>Larkmere Bathrooms – Business Card</title>
<link rel="stylesheet" href="https://fonts.googleapis.com/css2?family=Montserrat:wght@400;500;700&display=swap">
<style>
  :root {
    --stage: #2e2e30;
    --card-white: #ffffff;
    --card-silver: #c8c8c9;
    --silver-ink: #8e8e90;
    --brand-blue: #1470bd;
    --band-grey: #cfcfd1;
    --ink: #2a2a2a;
  }
  * { box-sizing: border-box; margin: 0; padding: 0; }
  html, body {
    width: 1200px; height: 1186px; overflow: hidden;
    background: var(--stage);
    font-family: "Montserrat", sans-serif;
  }
  .stage { position: relative; width: 1200px; height: 1186px; }
  .card {
    position: absolute; left: 160px; width: 880px; height: 503px;
    border-radius: 28px; overflow: hidden;
  }

  /* Back of card */
  .card-back { top: 60px; background: var(--card-silver); }
  .card-back .wordmark {
    position: absolute; inset: 0;
    display: flex; align-items: center; justify-content: center; gap: 20px;
  }
  .card-back .mark-square { width: 40px; height: 40px; background: var(--silver-ink); flex: none; }
  .card-back .brand-name {
    font-weight: 500; font-size: 44px; letter-spacing: 5px;
    color: var(--silver-ink); text-transform: uppercase; white-space: nowrap;
  }

  /* Front of card */
  .card-front { top: 623px; background: var(--card-white); }
  .front-logo {
    position: absolute; left: 60px; top: 84px;
    display: flex; align-items: center; gap: 16px;
  }
  .front-logo .mark-square { width: 30px; height: 30px; background: var(--brand-blue); }
  .front-logo .brand-name {
    font-weight: 500; font-size: 32px; letter-spacing: 3px;
    color: var(--brand-blue); text-transform: uppercase; white-space: nowrap;
  }
  .tagline {
    position: absolute; right: 40px; top: 232px;
    font-size: 20px; color: var(--ink);
  }
  .divider {
    position: absolute; left: 250px; right: 0; top: 270px;
    height: 2px; background: var(--brand-blue);
  }
  .card-bands { position: absolute; inset: 0; width: 880px; height: 503px; }
  .licence {
    position: absolute; right: 32px; top: 311px;
    font-size: 19px; line-height: 26px; color: #fff; letter-spacing: 0.5px;
    white-space: nowrap;
  }
  .person { position: absolute; left: 60px; top: 278px; }
  .person .name { font-weight: 700; font-size: 30px; line-height: 36px; color: var(--brand-blue); }
  .person .role { font-size: 20px; line-height: 24px; color: var(--ink); margin-top: 2px; }
  .contact-list { list-style: none; margin-top: 20px; }
  .contact-list li {
    display: flex; align-items: center; gap: 14px;
    font-size: 20px; line-height: 24px; color: var(--ink); margin-bottom: 8px;
  }
  .contact-list svg { width: 18px; height: 18px; fill: var(--brand-blue); flex: none; }
</style>
</head>
<body>
<main class="stage">
  <section class="card card-back" aria-label="Card back">
    <div class="wordmark">
      <span class="mark-square"></span>
      <span class="brand-name">Larkmere Bathrooms</span>
    </div>
  </section>

  <section class="card card-front" aria-label="Card front">
    <svg class="card-bands" viewBox="0 0 880 503" aria-hidden="true">
      <polygon points="652,298 880,298 880,352 644,352" fill="var(--brand-blue)"/>
      <polygon points="230,474 880,392 880,404 230,486" fill="var(--band-grey)"/>
      <polygon points="0,494 880,410 880,503 0,503" fill="var(--brand-blue)"/>
    </svg>

    <div class="front-logo">
      <span class="mark-square"></span>
      <span class="brand-name">Larkmere Bathrooms</span>
    </div>

    <p class="tagline">Renovation specialists</p>
    <div class="divider"></div>
    <p class="licence">Lic # 582143K</p>

    <div class="person">
      <p class="name">Adrian Holt</p>
      <p class="role">CEO &amp; Founder</p>
      <ul class="contact-list">
        <li>
          <svg viewBox="0 0 24 24"><path d="M6.6 10.8a15.1 15.1 0 0 0 6.6 6.6l2.2-2.2a1 1 0 0 1 1-.25 11.4 11.4 0 0 0 3.6.57 1 1 0 0 1 1 1V20a1 1 0 0 1-1 1A17 17 0 0 1 3 4a1 1 0 0 1 1-1h3.5a1 1 0 0 1 1 1c0 1.25.2 2.45.57 3.57a1 1 0 0 1-.25 1z"/></svg>
          <span>0487265920</span>
        </li>
        <li>
          <svg viewBox="0 0 24 24"><path d="M2 5h20v14H2z"/><path d="M3 6l9 7 9-7" fill="none" stroke="#fff" stroke-width="1.6"/></svg>
          <span>Tobin@larkmerebathrooms.com.au</span>
        </li>
      </ul>
    </div>
  </section>
</main>
</body>
</html>
```